Business Card Design

We are looking for a double sided business card.

On one side would be our logo

On the Other Side

Martin Kolby
Sales and Marketing

Phone/Text Logo and 530-418-2763
Email Logo and info@plumvalepets.com
Website Logo and www.plumvalepets.com
Facebook Logo and plumvale pets
Instagram Logo and plumvale_pets

Target Market(s)

Pet owners

Contact Information for Business Card

In project description

Requirements
Must have
• Logo

```html
<!DOCTYPE html>
<html lang="en">
<head>
<meta charset="utf-8">
<title>Plumvale Pets – Business Card</title>
<link href="https://fonts.googleapis.com/css2?family=Montserrat:wght@400;500;700&display=swap" rel="stylesheet">
<style>
  :root {
    --backdrop: #3b3b3b;
    --card: #060606;
    --orange: #f39a1e;
    --gold: #e2a324;
    --white: #f1f1f1;
  }
  * { box-sizing: border-box; margin: 0; padding: 0; }
  html, body { width: 1200px; height: 689px; overflow: hidden; }
  body {
    background: var(--backdrop);
    font-family: "Montserrat", sans-serif;
    color: var(--white);
    position: relative;
  }
  .card {
    position: absolute;
    top: 196px;
    width: 520px;
    height: 297px;
    background: var(--card);
    border-radius: 18px;
    box-shadow: 0 14px 30px rgba(0,0,0,.45);
    overflow: hidden;
  }
  .card--front { left: 50px; }
  .card--back { left: 630px; }

  .brand {
    display: flex;
    align-items: center;
    gap: 12px;
    color: var(--orange);
    font-weight: 700;
    letter-spacing: .02em;
  }
  .brand__dot {
    border-radius: 50%;
    background: var(--orange);
    flex: none;
  }
  .card--front .brand {
    position: absolute;
    inset: 0;
    justify-content: center;
    font-size: 42px;
  }
  .card--front .brand__dot { width: 26px; height: 26px; }

  .card--back .brand {
    position: absolute;
    left: 26px;
    top: 132px;
    font-size: 22px;
    gap: 8px;
  }
  .card--back .brand__dot { width: 14px; height: 14px; }

  .divider {
    position: absolute;
    left: 246px;
    top: 52px;
    width: 1px;
    height: 110px;
    background: var(--gold);
  }
  .contact {
    position: absolute;
    left: 268px;
    top: 46px;
  }
  .contact__name {
    color: var(--orange);
    font-weight: 700;
    font-size: 21px;
    line-height: 1.1;
  }
  .contact__role {
    font-size: 14px;
    margin-top: 4px;
  }
  .contact__list {
    list-style: none;
    margin-top: 10px;
    font-size: 13.5px;
  }
  .contact__list li {
    display: flex;
    align-items: center;
    gap: 8px;
    line-height: 21px;
  }
  .icon { width: 14px; height: 14px; flex: none; }

  .social {
    position: absolute;
    left: 60px;
    right: 40px;
    top: 196px;
    text-align: center;
  }
  .social__rule {
    display: flex;
    align-items: center;
    gap: 10px;
  }
  .social__rule::before, .social__rule::after {
    content: "";
    flex: 1;
    height: 1px;
    background: var(--gold);
  }
  .social__marks { display: flex; gap: 8px; }
  .social__mark {
    width: 14px; height: 14px;
    border-radius: 50%;
    background: var(--orange);
  }
  .social__handles {
    margin-top: 8px;
    font-size: 14.5px;
    line-height: 20px;
  }
</style>
</head>
<body>

  <section class="card card--front" aria-label="Card front">
    <div class="brand"><span class="brand__dot"></span>Plumvale Pets</div>
  </section>

  <section class="card card--back" aria-label="Card back">
    <div class="brand"><span class="brand__dot"></span>Plumvale Pets</div>
    <div class="divider"></div>

    <div class="contact">
      <p class="contact__name">Martin Kolby</p>
      <p class="contact__role">Sales and Marketing</p>
      <ul class="contact__list">
        <li>
          <svg class="icon" viewBox="0 0 16 16" aria-hidden="true"><path fill="var(--orange)" d="M3.6 1.5l2.3 2.6-1.3 1.6a9 9 0 0 0 5.7 5.7l1.6-1.3 2.6 2.3-1.4 2.1C7.5 14.4 1.6 8.5 1.5 2.9z"/></svg>
          530-418-2763
        </li>
        <li>
          <svg class="icon" viewBox="0 0 16 16" aria-hidden="true"><rect x="1" y="3" width="14" height="10" rx="1" fill="var(--orange)"/><path d="M1.5 3.8 8 9l6.5-5.2" fill="none" stroke="var(--card)" stroke-width="1.4"/></svg>
          info@plumvalepets.com
        </li>
        <li>
          <svg class="icon" viewBox="0 0 16 16" aria-hidden="true"><g fill="none" stroke="var(--orange)" stroke-width="1.5"><circle cx="8" cy="8" r="6.5"/><ellipse cx="8" cy="8" rx="3" ry="6.5"/><path d="M1.5 8h13"/></g></svg>
          www.plumvalepets.com
        </li>
      </ul>
    </div>

    <div class="social">
      <div class="social__rule">
        <span class="social__marks"><span class="social__mark"></span><span class="social__mark"></span></span>
      </div>
      <p class="social__handles">@plumvale pets<br>@plumvale pets</p>
    </div>
  </section>

</body>
</html>
```